Bright Path Therapies business cards and stationary

Need business cards and stationary designed to match previously made logo for for a new company based in Sydney NSW called 'Bright Path Therapies'.

We provide early intervention services and diagnostic assessment for children with disability and their families. I would like designs that are colourful and child friendly - possibly using feet/footprints/steps on a white background. The final design should communicate that we are family friendly, accepting and fun to work with.

Target Market(s)

Parents and Families
Teachers
Allied Health Professionals

Industry/Entity Type

Psychology

Contact Information for Business Card

Bright Path Therapies
www.brightpaththerapies.example
info@brightpaththerapies.example

Font styles to use
Sans Serif
Decorative
Script

Requirements
Must have
• Match the font and colour scheme of logo, along with footprint picture
Nice to have
• Clean and simple, while reflecting that I am working with families.
• Also- editable for when we make staff specific cards.

```html
<!DOCTYPE html>
<html lang="en">
<head>
<meta charset="utf-8">
<title>Bright Path Therapies – Business Cards</title>
<link href="https://fonts.googleapis.com/css2?family=Nunito+Sans:wght@400;600;700&display=swap" rel="stylesheet">
<style>
  :root {
    --page-bg: #e6e6e6;
    --card-bg: #0b0b0b;
    --pattern-a: #151515;
    --pattern-b: #1e1e1e;
    --brand-red: #ee4a3c;
    --brand-blue: #2b82d4;
    --brand-orange: #f39a2b;
    --brand-green: #7cc242;
    --text-light: #e8e8e8;
    --divider: #4a4a4a;
  }
  * { box-sizing: border-box; margin: 0; padding: 0; }
  html, body { width: 1200px; height: 1000px; overflow: hidden; }
  body {
    background: var(--page-bg);
    font-family: "Nunito Sans", Arial, sans-serif;
    position: relative;
  }
  .card {
    position: absolute;
    left: 269px;
    width: 662px;
    height: 379px;
    background: var(--card-bg);
    overflow: hidden;
    box-shadow: 0 3px 8px rgba(0,0,0,0.35);
  }
  .card--front { top: 108px; }
  .card--back { top: 520px; height: 380px; }
  .footprint-pattern {
    position: absolute;
    inset: 0;
    background: linear-gradient(135deg, var(--pattern-a), var(--pattern-b) 50%, var(--pattern-a));
  }
  .brand {
    position: absolute;
    left: 129px;
    display: flex;
    align-items: center;
    gap: 22px;
  }
  .card--front .brand { top: 140px; }
  .card--back .brand { top: 66px; }
  .brand__mark {
    width: 114px;
    height: 114px;
    border-radius: 50%;
    background: var(--brand-red);
    flex: none;
  }
  .brand__name {
    color: var(--brand-blue);
    font-weight: 600;
    font-size: 44px;
    line-height: 1.05;
    letter-spacing: 1px;
  }
  .person {
    position: absolute;
    right: 371px;
    top: 244px;
    text-align: right;
  }
  .person__name {
    color: var(--brand-red);
    font-weight: 700;
    font-size: 19px;
    letter-spacing: 0.5px;
    text-transform: uppercase;
  }
  .person__role {
    color: var(--text-light);
    font-size: 15px;
    margin-top: 4px;
  }
  .divider {
    position: absolute;
    left: 318px;
    top: 242px;
    width: 1px;
    height: 48px;
    background: var(--divider);
  }
  .contact {
    position: absolute;
    left: 344px;
    top: 238px;
    list-style: none;
    color: var(--text-light);
    font-size: 15px;
    line-height: 19.5px;
  }
  .contact li { display: flex; align-items: center; gap: 5px; }
  .contact svg { width: 11px; height: 11px; flex: none; }
  .colour-band {
    position: absolute;
    left: 0; right: 0; bottom: 0;
    height: 10px;
    display: flex;
  }
  .colour-band span { flex: 1; }
  .colour-band .blue { background: var(--brand-blue); }
  .colour-band .red { background: var(--brand-red); }
  .colour-band .orange { background: var(--brand-orange); }
  .colour-band .green { background: var(--brand-green); }
</style>
</head>
<body>

<section class="card card--front">
  <div class="footprint-pattern" role="img" aria-label="Faint repeating footprint pattern"></div>
  <div class="brand">
    <div class="brand__mark"></div>
    <div class="brand__name">Bright Path<br>Therapies</div>
  </div>
</section>

<section class="card card--back">
  <div class="footprint-pattern" role="img" aria-label="Faint repeating footprint pattern"></div>
  <div class="brand">
    <div class="brand__mark"></div>
    <div class="brand__name">Bright Path<br>Therapies</div>
  </div>

  <div class="person">
    <div class="person__name">Maren Holloway</div>
    <div class="person__role">Managing Director</div>
  </div>

  <div class="divider"></div>

  <ul class="contact">
    <li>
      <svg viewBox="0 0 12 12" aria-hidden="true"><path d="M3 1 L5 3.5 L4 4.8 Q5 7 7.2 8 L8.5 7 L11 9 L9.5 11 Q4 10.5 1 3 Z" fill="var(--brand-blue)"/></svg>
      020-555-0147
    </li>
    <li>
      <svg viewBox="0 0 12 12" aria-hidden="true"><rect x="0.5" y="2.5" width="11" height="7.5" fill="var(--brand-orange)"/><path d="M0.5 2.5 L6 7 L11.5 2.5" stroke="var(--card-bg)" stroke-width="1" fill="none"/></svg>
      info@brightpaththerapies.example
    </li>
    <li>
      <svg viewBox="0 0 12 12" aria-hidden="true"><circle cx="6" cy="6" r="5.5" fill="var(--brand-green)"/><path d="M0.5 6 H11.5 M6 0.5 V11.5 M6 0.5 Q2.5 6 6 11.5 M6 0.5 Q9.5 6 6 11.5" stroke="var(--card-bg)" stroke-width="0.8" fill="none"/></svg>
      www.brightpaththerapies.example
    </li>
  </ul>

  <div class="colour-band">
    <span class="blue"></span><span class="red"></span><span class="orange"></span><span class="green"></span>
  </div>
</section>

</body>
</html>
```